依頼詳細
【Tobiraのサービス特徴はこの3つ!】
●無料で請求書管理
請求書の作成・PDFダウンロードなどの機能はずっと無料でご利用になれます。顧客の数や、請求書の枚数に制限はありません。さらに有料プランなら見積り機能も使えます
●あんしんの印刷・郵送システム
Tobiraでは安全なドキュメントセンターで印刷、封入、封かん、発送を行なっています。それぞれの作業は機械が行うため請求書をの中身を人が見るということや人為的なミスはありません。詳しくはこちら
●どこでも請求書の作成・管理ができる
専用画面からログインすれば、書き方がわからなくてもテンプレートの必要事項を埋めるだけで出張先や自宅、iPad、スマートフォンなどからいつでも作成・編集できます。

---------------------------------------------------------------------------------

今回は、2種類のデザインを採用させていただきます。
1件10万円で、2種類の募集となりますので、
ドド~ンと総額20万円のキャンペーンとなります。
記載項目
■ 希望するデザイン
フリーランスのエンジニアさん、デザイナーさんが使いたくなる、オシャレで格好いい請求書の、オリジナルのデザインをご提案ください。

また、以下内容は請求書面として必要な事項となりますので必ず記載ください。
(現状の請求書のデータをアップロードしておりますので参照・活用ください)
・請求年月日
・請求先名称
・請求元(名前、住所、TEL、FAX、メールアドレス)
・請求元印影画像
・請求金額合計
・請求明細(20行、小計、消費税、合計金額)
・備考欄(3行)
・振込口座欄(1行)
希望イメージ
• +5 0 +5
• シンプル
複雑
• 単色
カラフル
• 暗い
明るい
• 日常
高級
• 遊び心
厳粛
• 未来的
伝統的
• 女性的
男性的
希望する色
色の指定はございません
納品ファイル
• イラストレーター形式 (.ai)
• フォトショップ形式 (.psd)
補足説明
■ 納品ファイルの希望
Illustrator形式、Photoshop形式、Fireworks形式
(最大容量は1024kbとしてそれ以下で作ってください)
依頼公開後の追記内容
■ 選んだ理由

bluewhistlerさんの作品は、どの業種でも使いやすく受け取り手も安心できるデザインということで選ばせて頂きました

もう一点は(http://www.kumoshi-hub.jp/work/proposal/5830417)になります。(現在システムの都合で当選にできていません)
k-atelierさんの作品は請求書のかっちりした感じに少し遊びを加えた感じのバランスがよく、採用しました。

■ 提案者全員のお礼・コメント

これほど多くの応募をいただけるとは思っておらずとても驚くとともに、感謝の気持でいっぱいです。

請求書のデザインということで、単純にデザイン性だけでは判断できず、どれも素敵な作品ばかりだったので選定には本当に時間がかかりました。

今回の当選作品以外にもTobira賞として10点ほど買取のオファーを出させて頂きます。どうぞよろしくおねがいします。

この度は本当にご応募ありがとうございました。

```html
<!DOCTYPE html>
<html lang="ja">
<head>
<meta charset="utf-8">
<title>請求書</title>
<link rel="stylesheet" href="https://fonts.googleapis.com/css2?family=Noto+Sans+JP:wght@400;500;700&display=swap">
<style>
:root{
  --ink:#1c1c1c;
  --paper:#ffffff;
  --line:#9a9a9a;
  --line-soft:#cfcfcf;
  --band:#e6e6e6;
  --band-dark:#d4d4d4;
  --seal:#d8232a;
  --sub:#555555;
}
*{box-sizing:border-box;margin:0;padding:0}
html,body{width:849px;height:1200px;overflow:hidden;background:var(--paper)}
body{font-family:"Noto Sans JP",sans-serif;color:var(--ink);position:relative}
.sheet{position:absolute;inset:0;border:1px solid var(--line-soft)}
.abs{position:absolute}
.label{background:var(--ink);color:var(--paper);font-size:12px;font-weight:500;display:flex;align-items:center;justify-content:center;letter-spacing:1px;flex:none}

/* title */
.title-rule{left:40px;top:52px;width:781px;height:2px;background:var(--ink)}
.title-char{top:22px;width:62px;height:62px;border-radius:50%;background:var(--ink);color:var(--paper);font-size:32px;font-weight:700;display:flex;align-items:center;justify-content:center}
.issue-row{top:38px;left:470px;display:flex;align-items:center;background:var(--paper);height:28px;font-size:15px;padding-left:6px}
.issue-row .label{height:22px;padding:0 8px}
.issue-row .val{padding:0 12px;white-space:nowrap}

/* client */
.client{left:40px;top:140px;width:390px;font-size:26px;font-weight:700;border-bottom:2px solid var(--ink);padding-bottom:4px}
.client small{font-size:22px;font-weight:500;margin-left:10px}
.invoice-no{left:40px;top:188px;display:flex;align-items:center;font-size:14px}
.invoice-no .label{width:76px;height:22px}
.invoice-no .val{padding-left:14px;border-bottom:1px solid var(--line);width:310px;height:22px;line-height:22px}
.greeting{left:40px;top:218px;font-size:13px;line-height:21px}

/* issuer */
.issuer-name{left:481px;top:76px;font-size:18px;font-weight:700;white-space:nowrap}
.issuer-addr{left:481px;top:108px;font-size:12px;line-height:18px;color:var(--sub)}
.seal{left:748px;top:72px;width:68px;height:110px;background:var(--seal);opacity:.85}
.contact{left:481px;display:flex;align-items:center;font-size:13px}
.contact .label{height:20px;padding:0 7px;font-size:11px}
.contact .val{padding:0 10px;border-bottom:1px solid var(--line);height:20px;line-height:20px;white-space:nowrap}

/* due band */
.due-band{left:40px;top:272px;width:781px;height:38px;background:var(--band);border-top:3px solid var(--ink);border-bottom:3px solid var(--ink);display:flex;align-items:center}
.due-band .label{height:26px;width:96px;margin-left:6px}
.due-band .date{width:176px;text-align:center;font-size:16px;white-space:nowrap}
.due-band .total{flex:1;height:26px;margin:0 6px;background:var(--paper);text-align:right;font-size:24px;font-weight:700;line-height:26px;padding-right:18px}

/* table */
.items{left:40px;top:330px;width:781px;border-collapse:collapse;font-size:12px}
.items th{background:var(--band-dark);height:28px;font-weight:500;border:1px solid var(--line);letter-spacing:2px}
.items td{height:31px;border-left:1px solid var(--line);border-right:1px solid var(--line);border-bottom:1px dotted var(--line-soft);padding:0 8px}
.items tr:last-child td{border-bottom:1px solid var(--line)}
.items .num{text-align:right}
.c-name{width:440px}.c-qty{width:92px}.c-price{width:117px}.c-amount{width:132px}

/* remarks & totals */
.remarks{left:40px;top:996px;font-size:12px;line-height:24px;color:var(--sub)}
.totals{left:531px;top:992px;width:290px;border-collapse:collapse;font-size:13px}
.totals th{background:var(--band);font-weight:500;border:1px solid var(--line);height:25px;width:158px;letter-spacing:4px}
.totals td{border:1px solid var(--line);text-align:right;padding-right:8px}
.totals tr.grand th,.totals tr.grand td{border-top:2px solid var(--ink);font-weight:700}

/* bank */
.bank{left:40px;top:1126px;width:781px;height:32px;background:var(--band);display:flex;align-items:center;font-size:13px;border-top:2px solid var(--ink);border-bottom:2px solid var(--ink)}
.bank .label{height:32px;width:70px}
.bank .val{padding-left:18px;letter-spacing:1px;white-space:nowrap}
</style>
</head>
<body>
<div class="sheet">

  <div class="abs title-rule"></div>
  <div class="abs title-char" style="left:40px">請</div>
  <div class="abs title-char" style="left:120px">求</div>
  <div class="abs title-char" style="left:200px">書</div>

  <div class="abs issue-row">
    <span class="label">発行日</span><span class="val">2013 年 05 月 11 日</span>
    <span class="label">ページ</span><span class="val">1 / 1</span>
  </div>

  <div class="abs client">サンプル株式会社<small>様</small></div>
  <div class="abs invoice-no"><span class="label">請求番号</span><span class="val">20130511-005</span></div>
  <p class="abs greeting">下記内容にてご請求書を発行いたします。<br>ご確認の程、よろしくお願い申し上げます。</p>

  <div class="abs issuer-name">ミナトワークス株式会社</div>
  <p class="abs issuer-addr">〒460-0008<br>愛知県名古屋市中区<br>栄４丁目８番２号<br>ミナトビル２F</p>
  <div class="abs seal" role="img" aria-label="発行元の社印"></div>

  <div class="abs contact" style="top:210px">
    <span class="label">TEL</span><span class="val">052-555-0142</span>
    <span class="label">FAX</span><span class="val">052-555-0142</span>
  </div>
  <div class="abs contact" style="top:238px">
    <span class="label">e-MAIL</span><span class="val" style="width:240px">office@minatoworks.example</span>
  </div>

  <div class="abs due-band">
    <span class="label">お支払期限</span>
    <span class="date">2013 年 05 月 31 日</span>
    <span class="label">ご請求金額</span>
    <span class="total">¥ 84,000ー</span>
  </div>

  <table class="abs items">
    <thead>
      <tr><th class="c-name">品 番 ・ 品 名</th><th class="c-qty">数 量</th><th class="c-price">単 価</th><th class="c-amount">金 額</th></tr>
    </thead>
    <tbody>
      <tr><td>デザイン</td><td class="num">1</td><td class="num">20,000</td><td class="num">20,000</td></tr>
      <tr><td>企画・材料費用</td><td class="num">1</td><td class="num">60,000</td><td class="num">60,000</td></tr>
      <tr><td></td><td></td><td></td><td></td></tr>
      <tr><td></td><td></td><td></td><td></td></tr>
      <tr><td></td><td></td><td></td><td></td></tr>
      <tr><td></td><td></td><td></td><td></td></tr>
      <tr><td></td><td></td><td></td><td></td></tr>
      <tr><td></td><td></td><td></td><td></td></tr>
      <tr><td></td><td></td><td></td><td></td></tr>
      <tr><td></td><td></td><td></td><td></td></tr>
      <tr><td></td><td></td><td></td><td></td></tr>
      <tr><td></td><td></td><td></td><td></td></tr>
      <tr><td></td><td></td><td></td><td></td></tr>
      <tr><td></td><td></td><td></td><td></td></tr>
      <tr><td></td><td></td><td></td><td></td></tr>
      <tr><td></td><td></td><td></td><td></td></tr>
      <tr><td></td><td></td><td></td><td></td></tr>
      <tr><td></td><td></td><td></td><td></td></tr>
      <tr><td></td><td></td><td></td><td></td></tr>
      <tr><td></td><td></td><td></td><td></td></tr>
    </tbody>
  </table>

  <p class="abs remarks">サンプル（備考欄１行目）<br>サンプル（備考欄２行目）<br>振込手数料はご負担願います。</p>

  <table class="abs totals">
    <tr><th>小　計</th><td>80,000</td></tr>
    <tr><th>消 費 税（5%）</th><td>4,000</td></tr>
    <tr class="grand"><th>合 計 金 額</th><td>84,000</td></tr>
  </table>

  <div class="abs bank">
    <span class="label">振込先</span>
    <span class="val">日本ジャパン銀行　中央支店　普通口座　01234567　サンプル（カ）</span>
  </div>

</div>
</body>
</html>
```